Eavestone screen porch

Can you please design a flyer for me promoting my screen porch businessPlease remove the seamless gutters word from the title and add “screen porches” I have added the logo and a bunch of pictures from projects that I have done in the past. You can use words like Hillcrest Screen porches, etc

Target Market(s)

homeowners, contractors, builders

Industry/Entity Type

Construction

Requirements
Must have
• Dov Kerring
• Eavestone Gutters
• 2937 Old Hwy 52 N, Greer, SC 29607
• 864-307-6184
Nice to have
• A few colors maybe 3 most
• nice looking font

```html
<!DOCTYPE html>
<html lang="en">
<head>
<meta charset="utf-8">
<title>Eavestone Screen Porch Enclosures</title>
<link href="https://fonts.googleapis.com/css2?family=Bree+Serif&family=Lato:wght@400;700&family=Roboto:wght@400;500;700&display=swap" rel="stylesheet">
<style>
  :root {
    --red: #dc1b2f;
    --ink: #231f20;
    --paper: #ffffff;
    --backdrop: #e2e2e2;
    --body: #3a3a3a;
    --hero-a: #e4603f;
    --hero-b: #c95437;
  }
  * { margin: 0; padding: 0; box-sizing: border-box; }
  html, body { width: 1200px; height: 1200px; overflow: hidden; background: var(--backdrop); }
  .flyer {
    position: absolute; left: 186px; top: 20px;
    width: 827px; height: 1160px;
    background: var(--paper); overflow: hidden;
    font-family: "Lato", sans-serif;
  }
  .hero {
    position: absolute; left: 0; top: 154px; width: 827px; height: 398px;
    background: linear-gradient(135deg, var(--hero-a) 0%, var(--hero-b) 100%);
  }
  .brand-box {
    position: absolute; left: 0; top: 0; width: 316px; height: 171px;
    background: var(--paper);
    display: flex; align-items: center; justify-content: center; gap: 12px;
  }
  .brand-mark { width: 22px; height: 22px; background: var(--red); }
  .brand-name { font-family: "Bree Serif", serif; font-size: 44px; color: var(--red); }
  .title-box {
    position: absolute; left: 316px; top: 0; width: 511px; height: 154px;
    background: var(--red);
  }
  .title {
    position: absolute; left: 56px; top: 26px;
    font-family: "Bree Serif", serif; font-weight: 400; font-size: 54px; line-height: 56px;
    color: var(--paper); letter-spacing: 0.5px;
  }
  .gallery { position: absolute; left: 0; top: 552px; }
  .copy {
    position: absolute; top: 756px;
    font-size: 12.6px; line-height: 16.3px; color: var(--body); text-align: justify;
  }
  .copy p + p { margin-top: 15px; }
  .copy-left { left: 36px; width: 335px; }
  .copy-right { left: 415px; width: 376px; }
  .benefits-title {
    position: absolute; left: 415px; top: 854px;
    font-family: "Bree Serif", serif; font-size: 26px; color: var(--red); font-weight: 400;
  }
  .benefits {
    position: absolute; left: 415px; top: 895px; width: 380px;
    list-style: none; display: grid; grid-template-columns: 248px 132px; row-gap: 6px;
    font-family: "Bree Serif", serif; font-size: 19px; line-height: 24px; color: var(--ink);
  }
  .benefits li { display: flex; gap: 8px; }
  .benefits svg { flex: none; margin-top: 5px; }
  .footer { position: absolute; left: 0; top: 1025px; width: 827px; height: 135px; }
  .footer-bg { position: absolute; left: 0; top: 0; }
  .contact-person { position: absolute; left: 37px; top: 8px; color: var(--paper); font-family: "Roboto", sans-serif; }
  .contact-name { font-size: 31px; font-weight: 500; }
  .contact-company { font-size: 18px; font-weight: 500; margin-top: 6px; }
  .contact-line { display: flex; align-items: center; gap: 6px; font-size: 18px; margin-top: 12px; letter-spacing: 0.3px; }
  .contact-reach { position: absolute; left: 466px; top: 8px; color: var(--paper); font-family: "Roboto", sans-serif; }
  .contact-reach .row { display: flex; align-items: center; gap: 8px; font-size: 18px; margin-top: 9px; }
  .contact-reach .phone { font-size: 32px; font-weight: 500; margin-top: 0; }
</style>
</head>
<body>
<div class="flyer">
  <div class="hero" role="img" aria-label="Photo of a red tiled roof edge with copper gutters and downspout"></div>

  <div class="brand-box">
    <span class="brand-mark"></span>
    <span class="brand-name">Eavestone</span>
  </div>

  <div class="title-box">
    <h1 class="title">SCREEN PORCH<br>ENCLOSURES</h1>
  </div>

  <svg class="gallery" width="827" height="190" viewBox="0 0 827 190">
    <polygon points="0,0 827,0 827,29 0,100" fill="var(--red)"/>
    <polygon points="43,24 291,24 256,183 8,183" fill="var(--ink)"/>
    <polygon points="48,28 285,28 252,179 13,179" fill="#5e6a6e" role="img" aria-label="Photo of a gabled screened porch with cable railing"/>
    <polygon points="305,24 553,24 518,183 270,183" fill="var(--ink)"/>
    <polygon points="310,28 547,28 514,179 275,179" fill="#cfcbb9" role="img" aria-label="Photo of a screened porch on a cream sided house"/>
    <polygon points="567,24 815,24 780,183 532,183" fill="var(--ink)"/>
    <polygon points="572,28 809,28 776,179 537,179" fill="#a9aca6" role="img" aria-label="Photo of a raised white screened porch with stairs"/>
  </svg>

  <div class="copy copy-left">
    <p>Adding a screened in porch to your home helps maximize the size of your lot by creating more habitable space. You will be able to utilize your new porch almost all year round, especially with the predictive warm weather patterns of Greenville &amp; Spartanburg, SC. A screened in porch is something future homebuyers will be looking for within these areas due to their functionality; this in turn increases the value of your home. Choosing the right home improvements to invest in now will help you get the most return on your property when you do decide to sell.</p>
    <p>We offer free estimates, so you may as well give us call us today to explore your options of screened-in porches!</p>
  </div>

  <div class="copy copy-right">
    <p>We specialize in the installation of screened in porch enclosures, which add property value and curb appeal to any home. They allow homeowners to enjoy the outdoors without having to swat mosquitoes and bugs away or suffer from the elements like rain or strong winds.</p>
  </div>

  <h2 class="benefits-title">Benefits of Screened in Porches</h2>
  <ul class="benefits">
    <li><svg width="13" height="13" viewBox="0 0 14 14"><circle cx="7" cy="7" r="7" fill="var(--red)"/><path d="M5 4l3 3-3 3" stroke="#fff" stroke-width="2" fill="none"/></svg>Privacy</li>
    <li><svg width="13" height="13" viewBox="0 0 14 14"><circle cx="7" cy="7" r="7" fill="var(--red)"/><path d="M5 4l3 3-3 3" stroke="#fff" stroke-width="2" fill="none"/></svg>No Bugs</li>
    <li><svg width="13" height="13" viewBox="0 0 14 14"><circle cx="7" cy="7" r="7" fill="var(--red)"/><path d="M5 4l3 3-3 3" stroke="#fff" stroke-width="2" fill="none"/></svg>Year-Round Use</li>
    <li><svg width="13" height="13" viewBox="0 0 14 14"><circle cx="7" cy="7" r="7" fill="var(--red)"/><path d="M5 4l3 3-3 3" stroke="#fff" stroke-width="2" fill="none"/></svg>Home Value</li>
    <li><svg width="13" height="13" viewBox="0 0 14 14"><circle cx="7" cy="7" r="7" fill="var(--red)"/><path d="M5 4l3 3-3 3" stroke="#fff" stroke-width="2" fill="none"/></svg>Extend Your<br>Living Space</li>
    <li><svg width="13" height="13" viewBox="0 0 14 14"><circle cx="7" cy="7" r="7" fill="var(--red)"/><path d="M5 4l3 3-3 3" stroke="#fff" stroke-width="2" fill="none"/></svg>New Family<br>Space</li>
  </ul>

  <div class="footer">
    <svg class="footer-bg" width="827" height="135" viewBox="0 0 827 135">
      <rect width="827" height="135" fill="var(--red)"/>
      <polygon points="0,0 440,0 390,135 0,135" fill="var(--ink)"/>
    </svg>
    <div class="contact-person">
      <div class="contact-name">Dov Kerring</div>
      <div class="contact-company">Eavestone Gutters</div>
      <div class="contact-line">
        <svg width="20" height="20" viewBox="0 0 20 20"><circle cx="10" cy="10" r="10" fill="#fff"/><path d="M10 4.5a3.5 3.5 0 0 0-3.5 3.5c0 2.6 3.5 6.5 3.5 6.5s3.5-3.9 3.5-6.5A3.5 3.5 0 0 0 10 4.5z" fill="var(--ink)"/><circle cx="10" cy="8" r="1.3" fill="#fff"/></svg>
        2937 Old Hwy 52 N, Greer, SC 29607
      </div>
    </div>
    <div class="contact-reach">
      <div class="row phone">
        <svg width="22" height="22" viewBox="0 0 22 22"><circle cx="11" cy="11" r="11" fill="#fff"/><path d="M7.5 5.5l2 2.5-1.2 1.4a7 7 0 0 0 4.3 4.3l1.4-1.2 2.5 2-1.3 2c-4.8-.4-8.5-4.1-9-9z" fill="var(--red)"/></svg>
        864-307-6184
      </div>
      <div class="row">
        <svg width="20" height="20" viewBox="0 0 20 20"><circle cx="10" cy="10" r="10" fill="#fff"/><rect x="5" y="6.5" width="10" height="7" fill="var(--red)"/><path d="M5 6.5l5 4 5-4" stroke="#fff" stroke-width="1.2" fill="none"/></svg>
        info@eavestonegutters.com
      </div>
      <div class="row">
        <svg width="20" height="20" viewBox="0 0 20 20" fill="none" stroke="#fff" stroke-width="1.4"><circle cx="10" cy="10" r="8.5"/><ellipse cx="10" cy="10" rx="3.8" ry="8.5"/><path d="M1.5 10h17M3 5.5h14M3 14.5h14"/></svg>
        www.eavestoneseamlessgutters.com
      </div>
    </div>
  </div>
</div>
</body>
</html>
```